Quarrow financial services, is a financial company that provides consultancy, brokerage services, and funding.

we will be providing the clients with insights, knowledge and data with regards to the financial markets.

with the brokerage services we will try to find the suitable counterparts that provide them with the best investments that suits their needs and expected return.

Target Market(s)

financial institutions, Corporates, high-net worth individuals

Industry/Entity Type

Financial Service

Contact Information for Business Card

Font styles to use
Other font styles liked:
• applemyungjo

Colors
00a990
848484

Requirements
Must have
• the logo at the back
Nice to have
• Finesse
Should not have
• boldness

```html
<!DOCTYPE html>
<html lang="en">
<head>
<meta charset="utf-8">
<title>Quarrow Financial Services – Business Card</title>
<link rel="stylesheet" href="https://fonts.googleapis.com/css2?family=Cormorant+Garamond:wght@400;500&family=Open+Sans:wght@400;600&display=swap">
<style>
  :root {
    --backdrop: #2b2b2b;
    --card: #161616;
    --card-edge: #222222;
    --accent: #79ab3c;
    --text-light: #e6e6e6;
    --text-soft: #bdbdbd;
    --divider: #2c2c2c;
    --mark-pale: #dfe9d2;
  }
  * { margin: 0; padding: 0; box-sizing: border-box; }
  html, body {
    width: 1200px; height: 900px; overflow: hidden;
    background: var(--backdrop);
  }
  .canvas {
    width: 1200px; height: 900px;
    display: flex; align-items: center; justify-content: center; gap: 60px;
  }
  .card {
    width: 520px; height: 300px;
    background: var(--card);
    border: 1px solid var(--card-edge);
    border-radius: 22px;
    position: relative;
    box-shadow: 0 18px 40px rgba(0,0,0,0.45);
  }
  /* Front side */
  .card-front { display: flex; }
  .brand-panel {
    width: 250px; height: 100%;
    display: flex; align-items: center; justify-content: center; gap: 12px;
    border-right: 1px solid var(--divider);
  }
  .brand-square {
    width: 14px; height: 14px; background: var(--mark-pale);
  }
  .brand-name {
    font-family: "Cormorant Garamond", serif;
    font-weight: 500; font-size: 30px; letter-spacing: 4px;
    color: var(--text-light); text-transform: uppercase;
  }
  .details {
    padding: 58px 0 0 42px;
    font-family: "Open Sans", sans-serif;
    color: var(--text-light);
  }
  .person-name { color: var(--accent); font-weight: 600; font-size: 17px; }
  .person-role { font-size: 13px; margin-top: 1px; }
  .address { font-size: 13px; line-height: 1.35; margin-top: 22px; }
  .contact-list { list-style: none; margin-top: 16px; }
  .contact-list li {
    display: flex; align-items: center; gap: 12px;
    font-size: 13px; line-height: 1.6;
  }
  .contact-list svg { width: 10px; height: 10px; fill: var(--accent); flex: none; }
  /* Back side */
  .card-back {
    display: flex; flex-direction: column; align-items: center; justify-content: center; gap: 6px;
  }
  .back-lockup { display: flex; align-items: center; gap: 14px; }
  .back-name {
    font-family: "Cormorant Garamond", serif;
    font-weight: 500; font-size: 40px; letter-spacing: 6px;
    color: var(--text-soft); text-transform: uppercase;
  }
  .back-sub {
    font-family: "Cormorant Garamond", serif;
    font-weight: 500; font-size: 14px; letter-spacing: 4px;
    color: var(--text-soft); text-transform: uppercase;
  }
</style>
</head>
<body>
<main class="canvas">
  <section class="card card-front">
    <div class="brand-panel">
      <span class="brand-square"></span>
      <span class="brand-name">Quarrow</span>
    </div>
    <div class="details">
      <p class="person-name">Daniel Hartley</p>
      <p class="person-role">Managing Director</p>
      <p class="address">P.O. Box 4418, Eastmere,<br>MI 49620</p>
      <ul class="contact-list">
        <li><svg viewBox="0 0 10 10"><path d="M2 0.5 L4 2.6 L3 3.8 Q4.2 6 6.2 7 L7.4 6 L9.5 8 L8.2 9.5 Q2.5 8.5 0.5 1.8 Z"/></svg>(044)-318-2207</li>
        <li><svg viewBox="0 0 10 10"><path d="M2.5 0 H7.5 V10 H2.5 Z M3.3 1 V8 H6.7 V1 Z"/></svg>123-904-5561</li>
        <li><svg viewBox="0 0 10 10"><path d="M0 2 H10 V8.5 H0 Z M0.8 2.6 L5 5.6 L9.2 2.6 Z" fill-rule="evenodd"/></svg>info@quarrowfs.com</li>
        <li><svg viewBox="0 0 10 10"><circle cx="5" cy="5" r="4.6"/></svg>www.quarrowfs.com</li>
      </ul>
    </div>
  </section>
  <section class="card card-back">
    <div class="back-lockup">
      <span class="brand-square"></span>
      <span class="back-name">Quarrow</span>
    </div>
    <p class="back-sub">Financial Services</p>
  </section>
</main>
</body>
</html>
```